Brindle Logistics Business Card Design

We are a trucking and warehousing company. We run freight in the US manly from the Pacific NW to TX and back up the the PNW. We also do warehousing where we store, move, and distribute freight. Looking for a clean and modern design of business card. We would like to look rich and elegant. Attached is our logo.

Industry/Entity Type

Trucking Company

Contact Information for Business Card

Looking for a clean and modern design of business card. We would like to look rich and elegant.

Font styles to use
Sans Serif

Colors

Designer to choose colors to be used in the design.

Requirements
Must have
• logo but it should not dominate the card
Should not have
• logo should not dominate the card

```html
<!DOCTYPE html>
<html lang="en">
<head>
<meta charset="utf-8">
<title>Brindle Logistics Business Card</title>
<link href="https://fonts.googleapis.com/css2?family=Arimo:wght@400;700&display=swap" rel="stylesheet">
<style>
  :root {
    --stage: #2a2a2c;
    --card: #ffffff;
    --brand-blue: #0a72bd;
    --brand-orange: #f7941d;
    --ink: #3d4046;
    --on-blue: #ffffff;
  }
  * { box-sizing: border-box; margin: 0; padding: 0; }
  html, body {
    width: 1200px; height: 880px; overflow: hidden;
    background: var(--stage);
    font-family: "Arimo", Arial, sans-serif;
  }
  .canvas { position: relative; width: 1200px; height: 880px; }
  .card {
    position: absolute;
    width: 600px; height: 343px;
    background: var(--card);
    border-radius: 18px;
    overflow: hidden;
    box-shadow: 0 18px 40px rgba(0,0,0,.45);
  }
  .card--front { left: 140px; top: 70px; }
  .card--back { left: 460px; top: 467px; }

  .wordmark {
    position: absolute;
    display: flex; align-items: center; gap: 14px;
    color: var(--ink);
    font-weight: 700;
    text-transform: uppercase;
    line-height: 1;
  }
  .wordmark__dot {
    width: 46px; height: 46px; border-radius: 50%;
    background: var(--brand-blue);
    flex: none;
  }
  .wordmark__name { font-size: 40px; letter-spacing: 3px; }
  .wordmark__sub { display: block; font-size: 17px; letter-spacing: 2.2px; margin-top: 6px; }
  .card--front .wordmark { left: 50%; top: 50%; transform: translate(-50%, -50%); }
  .card--back .wordmark { left: 40px; top: 92px; }

  .card__art { position: absolute; inset: 0; width: 600px; height: 343px; }

  .person { position: absolute; right: 36px; top: 30px; text-align: right; }
  .person__name { color: var(--brand-blue); font-weight: 700; font-size: 20px; letter-spacing: .5px; }
  .person__role { color: var(--brand-orange); font-size: 15px; margin-top: 3px; }

  .contact {
    position: absolute; right: 30px; top: 150px;
    color: var(--on-blue); font-size: 13.5px; line-height: 1.35;
    list-style: none; text-align: right;
  }
  .contact li { display: flex; justify-content: flex-end; align-items: center; gap: 8px; }
  .contact__icon {
    width: 16px; height: 16px; border-radius: 50%;
    background: var(--brand-orange);
    display: inline-flex; align-items: center; justify-content: center;
    flex: none;
  }
  .contact__icon svg { width: 10px; height: 10px; }
  .contact__spacer { width: 16px; flex: none; }
  .contact__address { margin-bottom: 6px; }
</style>
</head>
<body>
<main class="canvas">
  <section class="card card--front" aria-label="Card front">
    <div class="wordmark">
      <span class="wordmark__dot"></span>
      <span><span class="wordmark__name">Brindle</span><span class="wordmark__sub">Logistics, LLC</span></span>
    </div>
  </section>

  <section class="card card--back" aria-label="Card back">
    <svg class="card__art" viewBox="0 0 600 343" aria-hidden="true">
      <path d="M0 282 C150 290 262 250 282 170 C286 220 250 280 180 300 C120 315 60 312 0 310 Z" fill="var(--brand-orange)"/>
      <path d="M440 78 C350 90 320 190 285 250 C250 305 120 318 0 318 L0 343 L600 343 L600 76 Z" fill="var(--brand-blue)"/>
      <path d="M470 72 C370 92 345 210 300 268 C265 310 200 322 135 330" fill="none" stroke="#fff" stroke-width="4"/>
    </svg>

    <div class="wordmark">
      <span class="wordmark__dot"></span>
      <span><span class="wordmark__name">Brindle</span><span class="wordmark__sub">Logistics, LLC</span></span>
    </div>

    <div class="person">
      <p class="person__name">MARCUS HALE</p>
      <p class="person__role">President &amp; CEO</p>
    </div>

    <ul class="contact">
      <li class="contact__address"><span>PO BOX 418, Cedar Street<br>5th Lane, Portland</span><span class="contact__spacer"></span></li>
      <li><span>+01 5550 2741</span>
        <span class="contact__icon"><svg viewBox="0 0 10 10"><path d="M2 1 L4 1 L4.6 3 L3.5 3.8 C4 5 5 6 6.2 6.5 L7 5.4 L9 6 L9 8 C5 8.5 1.5 5 2 1 Z" fill="#fff"/></svg></span></li>
      <li><span>info@brindlefreight.com</span>
        <span class="contact__icon"><svg viewBox="0 0 10 10"><rect x="1" y="2.5" width="8" height="5.5" fill="none" stroke="#fff" stroke-width="1"/><path d="M1 2.5 L5 5.6 L9 2.5" fill="none" stroke="#fff" stroke-width="1"/></svg></span></li>
      <li><span>www.brindlefreight.com</span>
        <span class="contact__icon"><svg viewBox="0 0 10 10"><circle cx="5" cy="5" r="3.8" fill="none" stroke="#fff" stroke-width="1"/><path d="M1.2 5 H8.8 M5 1.2 C3 3.5 3 6.5 5 8.8 M5 1.2 C7 3.5 7 6.5 5 8.8" fill="none" stroke="#fff" stroke-width=".8"/></svg></span></li>
    </ul>
  </section>
</main>
</body>
</html>
```